Dale's Business Card Design For Businesses and Customers

Create a world class business card that will engage both businesses and customers. The card should be demonstrative of a serious business person and will lead all who are given the card to make contact. It should be both friendly and powerful. The colors must match or compliment the logo. If there are any other questions, please advise and I will provide a response.

Target Market(s)

Businesses and customers

Industry/Entity Type

Restaurant

Contact Information for Business Card

Front Side:
Sir Howard "Dale" Penrose, Founder

2716 Birchmont Court
Upper Fenwick, MD 20519

301.555.0148 DC Cell
404.555.0192 ATL Cell
888.555.0173 Toll-Free Fax
dale@kettlebrookgrill.example

www.kettlebrookgrill.example

Back:
Logo
www.kettlebrookgrill.example

Font styles to use
Serif

Colors

Designer to choose colors to be used in the design.

Requirements
Must have
• Card must be classy and highlight the website and contact information.
Nice to have
• Nice, clean, and classy like the logo.

```html
<!DOCTYPE html>
<html lang="en">
<head>
<meta charset="utf-8">
<title>Dale's Business Card</title>
<link href="https://fonts.googleapis.com/css2?family=Libre+Baskerville&display=swap" rel="stylesheet">
<style>
  :root {
    --blush: #fde8e2;
    --cocoa: #3a130c;
    --white: #ffffff;
    --ink: #2a0f09;
  }
  * { margin: 0; padding: 0; box-sizing: border-box; }
  html, body { width: 909px; height: 1200px; overflow: hidden; background: var(--white); }
  body { position: relative; font-family: "Libre Baskerville", "Baskerville", Georgia, serif; color: var(--ink); }

  .card { position: absolute; background: var(--blush); overflow: hidden; }
  .card-front { left: 0; top: 0; width: 902px; height: 551px; }
  .card-back { left: 4px; top: 645px; width: 902px; height: 552px; }

  .brand { position: absolute; text-align: center; }
  .brand-disc { width: 212px; height: 212px; border-radius: 50%; background: var(--cocoa); margin: 0 auto; }
  .brand-name { font-size: 58px; line-height: 1; margin-top: 22px; color: var(--cocoa); }
  .card-front .brand { left: 133px; top: 134px; width: 212px; }
  .card-back .brand { left: 347px; top: 80px; width: 212px; }

  .name-band { position: absolute; left: 490px; top: 0; width: 412px; height: 105px; background: var(--cocoa); color: var(--blush); text-align: center; padding-top: 12px; }
  .name-first { font-size: 45px; line-height: 1; }
  .name-last { font-size: 31px; line-height: 1.1; }

  .contact-row { position: absolute; left: 490px; display: flex; align-items: center; }
  .contact-icon { width: 60px; height: 60px; background: var(--cocoa); display: flex; align-items: center; justify-content: center; flex-shrink: 0; }
  .contact-icon svg { width: 36px; height: 36px; }
  .contact-text { margin-left: 22px; font-size: 18px; line-height: 1.25; }
  .contact-text.small { font-size: 15.5px; line-height: 1.45; }
  .row-email { top: 143px; }
  .row-phone { top: 236px; }
  .row-web { top: 331px; }
  .row-address { top: 426px; }

  .footer-band { position: absolute; left: 0; bottom: 0; width: 902px; height: 122px; }
  .footer-url { position: absolute; left: 0; right: 0; bottom: 24px; text-align: center; color: var(--blush); font-size: 29px; }
</style>
</head>
<body>

<section class="card card-front">
  <div class="brand">
    <div class="brand-disc"></div>
    <div class="brand-name">Dale's</div>
  </div>

  <header class="name-band">
    <div class="name-first">Sir Howard</div>
    <div class="name-last">"Dale" Penrose</div>
  </header>

  <div class="contact-row row-email">
    <div class="contact-icon">
      <svg viewBox="0 0 36 36" fill="none" stroke="#fff" stroke-width="2">
        <rect x="4" y="9" width="28" height="18"/>
        <path d="M4 9 L18 20 L32 9 M4 27 L14 17 M32 27 L22 17"/>
      </svg>
    </div>
    <div class="contact-text">dale@kettlebrookgrill.example</div>
  </div>

  <div class="contact-row row-phone">
    <div class="contact-icon">
      <svg viewBox="0 0 36 36" fill="#fff">
        <path d="M12 6 L17 6 L18 12 L15 14 Q16 21 21 24 L23 21 L29 23 L28 29 Q17 31 10 20 Q7 12 12 6 Z"/>
      </svg>
    </div>
    <div class="contact-text small">301.555.0148 DC Cell<br>404.555.0192 ATL Cell<br>888.555.0173 Toll-Free Fax</div>
  </div>

  <div class="contact-row row-web">
    <div class="contact-icon">
      <svg viewBox="0 0 36 36" fill="none" stroke="#fff" stroke-width="1.8">
        <circle cx="18" cy="18" r="13"/>
        <ellipse cx="18" cy="18" rx="6" ry="13"/>
        <path d="M5 18 H31 M7 11 H29 M7 25 H29 M18 5 V31"/>
      </svg>
    </div>
    <div class="contact-text">www.kettlebrookgrill.example</div>
  </div>

  <div class="contact-row row-address">
    <div class="contact-icon">
      <svg viewBox="0 0 36 36" fill="none" stroke="#fff" stroke-width="2">
        <path d="M18 33 Q8 21 8 14 A10 10 0 0 1 28 14 Q28 21 18 33 Z"/>
        <circle cx="18" cy="14" r="4.5"/>
      </svg>
    </div>
    <div class="contact-text">2716 Birchmont Court<br>Upper Fenwick, MD 20519</div>
  </div>
</section>

<section class="card card-back">
  <div class="brand">
    <div class="brand-disc"></div>
    <div class="brand-name">Dale's</div>
  </div>

  <svg class="footer-band" viewBox="0 0 902 122" preserveAspectRatio="none">
    <rect x="0" y="0" width="902" height="16" fill="#ffffff"/>
    <rect x="0" y="16" width="902" height="106" fill="#3a130c"/>
    <path d="M405 0 L453 44 L501 0 L483 0 L453 27 L423 0 Z" fill="#ffffff"/>
    <path d="M423 0 L453 27 L483 0 Z" fill="#fde8e2"/>
  </svg>
  <div class="footer-url">www.kettlebrookgrill.example</div>
</section>

</body>
</html>
```